Bref créative
Business Cards and Stationery for The Cheerful Parcel
The Cheerful Parcel
Traditional
Nora Whitcomb
Chief Executive Officer
24817 Halvern
Dunmore, MI 4735-1186
nora@thecheerfulparcel.example
www.thecheerfulparcel.example
This is my logo in AI

```html
<!DOCTYPE html>
<html lang="en">
<head>
<meta charset="utf-8">
<title>The Cheerful Parcel – Business Card</title>
<link rel="stylesheet" href="https://fonts.googleapis.com/css2?family=Open+Sans:wght@400;600;700&display=swap">
<style>
  :root {
    --page-bg: #e9e6e3;
    --plum: #5c0b5e;
    --plum-deep: #4a084c;
    --blush: #f6aeb0;
    --blush-light: #fbc6c6;
    --paper: #ffffff;
    --ink-name: #5c0b5e;
    --ink-text: #3a2a33;
  }
  * { margin: 0; padding: 0; box-sizing: border-box; }
  html, body {
    width: 1200px; height: 900px; overflow: hidden;
    background: var(--page-bg);
    font-family: "Open Sans", Arial, sans-serif;
  }
  .business-card {
    position: absolute; left: 75px; top: 150px;
    width: 1050px; height: 600px;
    background: var(--paper);
    overflow: hidden;
    box-shadow: 0 6px 18px rgba(0,0,0,0.18);
  }
  .card-bands { position: absolute; inset: 0; }
  .brand {
    position: absolute; left: 60px; top: 70px;
    display: flex; align-items: center; gap: 14px;
    color: var(--blush-light);
    font-size: 26px; font-weight: 600;
  }
  .brand-dot {
    width: 22px; height: 22px; border-radius: 50%;
    background: var(--blush-light);
  }
  .holder {
    position: absolute; left: 130px; top: 300px;
  }
  .holder-name {
    font-size: 30px; font-weight: 700; color: var(--ink-name);
    line-height: 1.2;
  }
  .holder-title {
    font-size: 22px; font-weight: 400; color: var(--ink-text);
    margin-top: 4px;
  }
  .contact-list {
    position: absolute; left: 670px; top: 238px;
    list-style: none;
    font-size: 19px; color: var(--ink-text);
  }
  .contact-list li {
    display: flex; align-items: flex-start; gap: 10px;
    line-height: 30px;
  }
  .contact-icon {
    flex: none; width: 22px; height: 22px; margin-top: 4px;
  }
  .contact-address span { display: block; }
</style>
</head>
<body>
  <div class="business-card">
    <svg class="card-bands" width="1050" height="600" viewBox="0 0 1050 600" aria-hidden="true">
      <defs>
        <linearGradient id="blushFill" x1="0" y1="0" x2="1" y2="0">
          <stop offset="0" stop-color="#f4a3a6"/>
          <stop offset="1" stop-color="#fbc4c4"/>
        </linearGradient>
        <linearGradient id="plumFill" x1="0" y1="0" x2="1" y2="0">
          <stop offset="0" stop-color="#4a084c"/>
          <stop offset="1" stop-color="#5f0c61"/>
        </linearGradient>
      </defs>
      <rect x="0" y="0" width="1050" height="215" fill="url(#plumFill)"/>
      <polygon points="0,230 150,230 172,206 194,230 1050,230 1050,515 0,515" fill="url(#blushFill)"/>
    </svg>

    <div class="brand">
      <span class="brand-dot"></span>
      <span class="brand-name">The Cheerful Parcel</span>
    </div>

    <div class="holder">
      <p class="holder-name">Nora Whitcomb</p>
      <p class="holder-title">Chief Executive Officer</p>
    </div>

    <ul class="contact-list">
      <li class="contact-address">
        <svg class="contact-icon" viewBox="0 0 22 22" aria-hidden="true"><circle cx="11" cy="11" r="11" fill="#3a2a33"/><path d="M11 5a4 4 0 0 0-4 4c0 3 4 8 4 8s4-5 4-8a4 4 0 0 0-4-4z" fill="#fbc6c6"/><circle cx="11" cy="9" r="1.5" fill="#3a2a33"/></svg>
        <div><span>24817 Halvern</span><span>Dunmore, MI 4735-1186</span></div>
      </li>
      <li>
        <svg class="contact-icon" viewBox="0 0 22 22" aria-hidden="true"><circle cx="11" cy="11" r="11" fill="#3a2a33"/><path d="M7 6l2.5-.5 1.3 3-1.5 1a7 7 0 0 0 3.2 3.2l1-1.5 3 1.3L16 15c-5 .5-9.5-4-9-9z" fill="#fbc6c6"/></svg>
        <span>734-555-0142</span>
      </li>
      <li>
        <svg class="contact-icon" viewBox="0 0 22 22" aria-hidden="true"><circle cx="11" cy="11" r="11" fill="#3a2a33"/></svg>
        <span>3135550178</span>
      </li>
      <li>
        <svg class="contact-icon" viewBox="0 0 22 22" aria-hidden="true"><circle cx="11" cy="11" r="11" fill="#3a2a33"/><rect x="6" y="7" width="10" height="8" rx="1" fill="#fbc6c6"/><rect x="8" y="9" width="6" height="2" fill="#3a2a33"/></svg>
        <span>734-555-0196</span>
      </li>
      <li>
        <svg class="contact-icon" viewBox="0 0 22 22" aria-hidden="true"><circle cx="11" cy="11" r="11" fill="#3a2a33"/><rect x="5.5" y="7" width="11" height="8" fill="#fbc6c6"/><path d="M5.5 7l5.5 4.5L16.5 7" fill="none" stroke="#3a2a33" stroke-width="1.2"/></svg>
        <span>nora@thecheerfulparcel.example</span>
      </li>
      <li>
        <svg class="contact-icon" viewBox="0 0 22 22" aria-hidden="true"><circle cx="11" cy="11" r="11" fill="#3a2a33"/><circle cx="11" cy="11" r="5.5" fill="none" stroke="#fbc6c6" stroke-width="1.3"/><path d="M5.5 11h11M11 5.5c-2.5 3-2.5 8 0 11M11 5.5c2.5 3 2.5 8 0 11" fill="none" stroke="#fbc6c6" stroke-width="1.1"/></svg>
        <span>www.thecheerfulparcel.example</span>
      </li>
    </ul>
  </div>
</body>
</html>
```